Detail Shop Business card design

i need a business card design for my new detailing company called 'Brenner's Detail Shop'. i want an all black and white design . simple, direct and to the point. i want the designer to choose a fitting font to match the logothe front should have logo, address, phone and email and the back side should have a slogan and text indicating that we offer services on anything including cars, trucks, motorcycles and RVs. slogan will read "we take pride in your ride"
maybe also very small on the back side the IG icon with Brenners_Detail_Shop

phone 482.615.7734
address 7384 E Harlow Ave
Spokane WA 99342
email: BrennersDetail@quorvail.com

Target Market(s)

all ages , auto enthusiasts

Industry/Entity Type

Automotive

Contact Information for Business Card

the front should have logo, address, phone and email and the back side should have a slogan and text indicating that we offer services on anything including cars, trucks, motorcycles and RVs. slogan will read "we take pride in your ride"

phone 482.615.7734
address 7384 E Harlow Ave
Spokane WA 99342

Colors
000000
ffffff

Requirements
Must have
• bold font and very simple design with good spacing
Nice to have
• anything creative from the designer indicating we service any types of vehicles
Should not have
• any colors ,

```html
<!DOCTYPE html>
<html lang="en">
<head>
<meta charset="utf-8">
<title>Brenner's Detail Shop – Business Cards</title>
<link rel="stylesheet" href="https://fonts.googleapis.com/css2?family=Noto+Serif:ital,wght@0,400;0,700;1,400&display=swap">
<style>
  :root {
    --ink: #000000;
    --paper: #ffffff;
    --stage: #d6d6d6;
    --muted: #cfcfcf;
  }
  * { box-sizing: border-box; margin: 0; padding: 0; }
  html, body { width: 1200px; height: 900px; overflow: hidden; }
  body {
    background: var(--stage);
    font-family: "Noto Serif", Georgia, serif;
    position: relative;
  }
  .card {
    position: absolute;
    left: 250px;
    width: 700px;
    height: 400px;
    border-radius: 28px;
    overflow: hidden;
    background: var(--ink);
    color: var(--paper);
  }
  .card--front { top: 40px; }
  .card--back { top: 460px; }

  .front-shape { position: absolute; inset: 0; }

  .brand {
    position: absolute;
    left: 0; top: 0;
    width: 280px; height: 400px;
    display: flex; flex-direction: column;
    align-items: center; justify-content: center;
    gap: 18px;
    color: var(--ink);
  }
  .brand__dot {
    width: 64px; height: 64px;
    border-radius: 50%;
    background: var(--ink);
  }
  .brand__name {
    font-weight: 700;
    font-size: 26px;
    line-height: 1.2;
    text-align: center;
  }

  .contact {
    position: absolute;
    left: 360px; right: 30px; top: 0; bottom: 0;
    display: flex; flex-direction: column;
    align-items: center; justify-content: center;
    text-align: center;
  }
  .contact__name {
    font-weight: 700;
    font-size: 27px;
    letter-spacing: 1px;
    text-transform: uppercase;
  }
  .contact__role { font-size: 17px; margin-top: 2px; color: var(--muted); }
  .contact__line { font-size: 21px; line-height: 1.35; }
  .rule {
    width: 90px; height: 1px;
    background: var(--paper);
    margin: 16px auto;
  }

  .back {
    position: absolute; inset: 0;
    display: flex; flex-direction: column;
    align-items: center; justify-content: center;
    text-align: center;
  }
  .handle {
    display: flex; align-items: center; gap: 8px;
    font-style: italic; font-size: 16px;
  }
  .handle__dot {
    width: 12px; height: 12px; border-radius: 50%;
    background: var(--paper);
  }
  .slogan {
    font-weight: 700;
    font-size: 32px;
    letter-spacing: 1px;
    text-transform: uppercase;
  }
  .services {
    display: flex; gap: 18px;
    list-style: none;
    font-style: italic; font-size: 17px;
  }
  .services li::before { content: "\2022\00a0"; font-style: normal; }
</style>
</head>
<body>

  <section class="card card--front" aria-label="Business card front">
    <svg class="front-shape" width="700" height="400" viewBox="0 0 700 400" aria-hidden="true">
      <polygon points="0,0 270,0 320,200 270,400 0,400" fill="#ffffff"/>
      <polyline points="288,0 338,200 288,400" fill="none" stroke="#ffffff" stroke-width="5"/>
    </svg>
    <div class="brand">
      <span class="brand__dot"></span>
      <p class="brand__name">Brenner's<br>Detail Shop</p>
    </div>
    <div class="contact">
      <h1 class="contact__name">Dale Mercer</h1>
      <p class="contact__role">Owner</p>
      <span class="rule"></span>
      <p class="contact__line">482.615.7734</p>
      <p class="contact__line">BrennersDetail@quorvail.com</p>
      <span class="rule"></span>
      <p class="contact__line">7384 E Harlow Ave</p>
      <p class="contact__line">Spokane WA 99342</p>
    </div>
  </section>

  <section class="card card--back" aria-label="Business card back">
    <div class="back">
      <p class="handle"><span class="handle__dot"></span>Brenners_Detail_Shop</p>
      <span class="rule"></span>
      <h2 class="slogan">We Take Pride in Your Ride</h2>
      <span class="rule"></span>
      <ul class="services">
        <li>Cars</li>
        <li>Trucks</li>
        <li>Motorcycles</li>
        <li>RVs</li>
      </ul>
    </div>
  </section>

</body>
</html>
```